3 screens for iOS app

I need a settings screen, dashboard and leaderboard screen created for an iPhone fitness app that is nearing completion. I have the template in .psd format that needs to be adhered to for consistency, and there are wireframe sketches (literally pen & paper) that you will translate into .psd files for chopping up and adding into the app. Also I need this by Monday.

Settings Screen:

Using the template psd, I need a basic list similar to the setting screen example attached (no icons needed, just text). The list of settings in order are:
Disclaimer
Edit Profile
Feedback
Help!
Terms of Use
Privacy Policy
Push Notifications (switcher icon on/off)
Chatterly Posts (switcher icon on/off)
Quipster Posts (switcher icon on/off)
Zenvok Videos Channel
Log Out

Dashboard:
The dashboard tempalte is attached. This dashboard should be inserted between the Grey banner heading and the Orange 14min standard routine bar. It will shift the graph down. The graph should remain unchanged, all you need to do in sert a cool looking dashboard inbetween the grey and orange bars

Dashboard contents:

Three dials (similar to pulsora, stridewell etc - see attached as an example) that display your progress

Dial 1: Title: Week
Dial should change colour as score approaches goal (ideally from green to orange as per icon example attached but not necessarily if you can make it look better)
Inside the dial it needs to include
Total: 598
Goal: 2,000
Days left: 5

Dial 2: Title: Improvement
Inside the dial it needs to include:
Start: 350
PB: 700
+100% in bold, centered

Dial 3: Title: Belt
Inside the dial needs to include:
Total: 9,834
Goal: 25,000

Leaderboard Screen:

Again using the template, with the grey banner heading at the top and tab bar at the bottom:

The leaderboard should be divided into two sections. The first is for my personal scores (as a user). The second section is for all players scores.

Section 1:
- Light grey background, dark grey text. Column titles can be pressed to filter columns. When pressed title changes colour from grey to orange (bold). If you can highlight two of the column titles orange that will be good

Section 2:
- White background, dark grey text. Column titles can be pressed to filter columns.
- Row height should be quite small to fit a large number of names on the screen.

Column titles: (sorry the wireframe sketch text is tough to read)
Rank / Name / W/outs / Wins / Week / Total / Belt

Rank - numeric values from 1-999
Name - text field
W/outs - number from 1-999
Wins - number 1-999
Week - number 1 - 99,999
Total - number 1- 99,999
Belt - coloured dot (white, black, red, blue, green, yellow)

For more info, refer http://www.zenvok.example/ and download the old app (iphone only) for an idea what we're after.

Industry/Entity Type

Fitness

Colors
f68e4e

Requirements
Must have
• Use the .psd template provided. We're not looking for a redesign.
• The fonts are:
• LeckerliOne Regular
• LobsterTwo Bold
• MeriendaOne Regular
• MVBoli
• GothamExtraLight
• LobsterTwo
Nice to have
• The best dashboard of all time.
Should not have
• changes to fonts,

```html
<!DOCTYPE html>
<html lang="en">
<head>
<meta charset="utf-8">
<title>Dashboard</title>
<link rel="stylesheet" href="https://fonts.googleapis.com/css2?family=Montserrat:wght@300;400;500;600&display=swap">
<style>
  :root {
    --header: #3d4249;
    --header-dark: #343940;
    --card-bg: #d9d9d9;
    --card: #ffffff;
    --ink: #3a3a3a;
    --accent: #e8972e;
    --banner: #e49525;
    --gear: #f0622a;
    --gauge-on: #5fbf25;
    --gauge-off: #e7e5ea;
    --chart-bg: #f7f7f7;
    --axis: #a9a9a9;
    --challenge: #f06a6a;
    --tab-label: #8a8e94;
    --tab-icon: #8d9197;
  }
  * { margin: 0; padding: 0; box-sizing: border-box; }
  html, body { width: 676px; height: 1200px; overflow: hidden; background: #fff; }
  body { font-family: "Montserrat", Arial, sans-serif; color: var(--ink); }
  .screen {
    position: absolute; left: 0; top: 0; width: 640px; height: 1136px;
    transform: scale(1.05625); transform-origin: 0 0; overflow: hidden;
  }
  .abs { position: absolute; }

  .nav { left: 0; top: 0; width: 640px; height: 130px; background: var(--header); color: #fff; }
  .status { left: 0; top: 0; width: 640px; height: 40px; font-size: 20px; font-weight: 500; }
  .status-time { left: 0; width: 640px; top: 8px; text-align: center; }
  .nav-title { left: 0; width: 640px; top: 62px; text-align: center; font-size: 36px; font-weight: 300; letter-spacing: 0.5px; }

  .stats { left: 0; top: 130px; width: 640px; height: 212px; background: var(--card-bg); }
  .stat-card { top: 8px; width: 201px; height: 194px; background: var(--card); box-shadow: 0 1px 2px rgba(0,0,0,.15); }
  .stat-title { top: 22px; left: 0; width: 100%; text-align: center; font-size: 15px; font-weight: 500; letter-spacing: .3px; }
  .gauge { top: 49px; left: 30px; }
  .stat-rows { top: 122px; left: 33px; right: 8px; font-size: 14.5px; line-height: 20.5px; }
  .stat-row { display: flex; }
  .stat-row .label { width: 92px; }
  .stat-row .value { color: var(--accent); font-weight: 500; }

  .routine-bar { left: 0; top: 342px; width: 640px; height: 95px; background: var(--banner); color: #fff; }
  .routine-title { left: 0; width: 640px; top: 26px; text-align: center; font-size: 29px; font-weight: 600; }

  .chart { left: 0; top: 437px; width: 640px; height: 563px; background: var(--chart-bg); }
  .axis-label { left: 0; width: 42px; text-align: right; font-size: 14px; color: var(--axis); }
  .challenge-name { left: 0; width: 640px; top: 917px; text-align: center; font-size: 24px; color: var(--challenge); }
  .expand { left: 271px; top: 956px; width: 98px; height: 41px; background: var(--header); }
  .divider { left: 0; top: 1000px; width: 640px; height: 3px; background: var(--header); }
  .spacer { left: 0; top: 1003px; width: 640px; height: 33px; background: #fff; }

  .tabbar { left: 0; top: 1036px; width: 640px; height: 100px; background: var(--header); }
  .tab-label { top: 1104px; width: 140px; text-align: center; font-size: 19px; color: var(--tab-label); }
  .tab-label.active { color: #fff; }
</style>
</head>
<body>
<div class="screen">

  <header class="nav abs">
    <div class="status abs">
      <svg class="abs" style="left:8px;top:12px" width="110" height="18" viewBox="0 0 110 18">
        <g fill="#fff"><circle cx="6" cy="9" r="5"/><circle cx="19" cy="9" r="5"/><circle cx="32" cy="9" r="5"/><circle cx="45" cy="9" r="5"/><circle cx="58" cy="9" r="5"/></g>
        <path d="M80 4 a20 20 0 0 1 24 0 l-2.5 3 a16 16 0 0 0 -19 0 Z M84 9 a13 13 0 0 1 16 0 l-2.5 3 a9 9 0 0 0 -11 0 Z M89 14 l3 3.5 l3 -3.5 a5 5 0 0 0 -6 0Z" fill="#fff"/>
      </svg>
      <div class="status-time abs">9:00 AM</div>
      <svg class="abs" style="left:578px;top:10px" width="54" height="22" viewBox="0 0 54 22">
        <rect x="1" y="1" width="46" height="20" rx="3" fill="none" stroke="#fff" stroke-width="1.5"/>
        <rect x="3.5" y="3.5" width="41" height="15" rx="1.5" fill="#4cd964"/>
        <rect x="48.5" y="7" width="3" height="8" rx="1" fill="#fff"/>
      </svg>
    </div>
    <svg class="abs" style="left:14px;top:63px" width="46" height="46" viewBox="0 0 46 46" aria-label="Settings">
      <g fill="none" stroke="var(--gear)" stroke-width="3" stroke-linejoin="round">
        <path d="M20 3h6l1 6 4 2 5-3 4 4-3 5 2 4 6 1v6l-6 1-2 4 3 5-4 4-5-3-4 2-1 6h-6l-1-6-4-2-5 3-4-4 3-5-2-4-6-1v-6l6-1 2-4-3-5 4-4 5 3 4-2z"/>
        <circle cx="23" cy="23" r="7"/>
      </g>
    </svg>
    <h1 class="nav-title abs">Dashboard</h1>
  </header>

  <section class="stats abs">
    <div class="stat-card abs" style="left:11px">
      <div class="stat-title abs">THIS WEEK</div>
      <svg class="gauge abs" width="140" height="72" viewBox="0 0 140 72">
        <path d="M4 70 A66 66 0 0 1 136 70 Z" fill="var(--gauge-off)"/>
        <path d="M4 70 A66 66 0 0 1 59.7 4.8 L70 70 Z" fill="var(--gauge-on)"/>
        <circle cx="70" cy="70" r="19" fill="#fff"/>
      </svg>
      <div class="stat-rows abs">
        <div class="stat-row"><span class="label">Total:</span><span class="value">598</span></div>
        <div class="stat-row"><span class="label">Goal:</span><span class="value">2,000</span></div>
        <div class="stat-row"><span class="label">Days left:</span><span class="value">5</span></div>
      </div>
    </div>

    <div class="stat-card abs" style="left:222px">
      <div class="stat-title abs">IMPROVEMENT</div>
      <svg class="gauge abs" width="140" height="72" viewBox="0 0 140 72">
        <path d="M4 70 A66 66 0 0 1 136 70 Z" fill="var(--gauge-off)"/>
        <path d="M4 70 A66 66 0 0 1 59.7 4.8 L70 70 Z" fill="var(--gauge-on)"/>
        <circle cx="70" cy="70" r="19" fill="#fff"/>
      </svg>
      <div class="stat-rows abs">
        <div class="stat-row"><span class="label">Start:</span><span class="value">350</span></div>
        <div class="stat-row"><span class="label">PB:</span><span class="value">700</span></div>
        <div class="stat-row"><span class="label">Increase:</span><span class="value">+100%</span></div>
      </div>
    </div>

    <div class="stat-card abs" style="left:431px">
      <div class="stat-title abs">CURRENT BELT:WHITE</div>
      <svg class="gauge abs" width="140" height="72" viewBox="0 0 140 72">
        <path d="M4 70 A66 66 0 0 1 136 70 Z" fill="var(--gauge-off)"/>
        <path d="M4 70 A66 66 0 0 1 65.9 4.1 L70 70 Z" fill="var(--gauge-on)"/>
        <circle cx="70" cy="70" r="19" fill="#fff"/>
      </svg>
      <div class="stat-rows abs" style="left:30px">
        <div class="stat-row"><span class="label">Total Reps:</span><span class="value">9,834</span></div>
        <div class="stat-row"><span class="label">Goal:</span><span class="value">10,000</span></div>
        <div class="stat-row"><span class="label">Next Belt:</span><span class="value">YELLOW</span></div>
      </div>
    </div>
  </section>

  <section class="chart abs"></section>

  <div class="routine-bar abs">
    <svg class="abs" style="left:18px;top:30px" width="16" height="34" viewBox="0 0 16 34"><path d="M13 2 L3 17 L13 32" fill="none" stroke="#f5c98a" stroke-width="2"/></svg>
    <div class="routine-title abs">14:00 minute Standard Routine</div>
    <svg class="abs" style="left:606px;top:30px" width="16" height="34" viewBox="0 0 16 34"><path d="M3 2 L13 17 L3 32" fill="none" stroke="#f5c98a" stroke-width="2"/></svg>
  </div>
  <svg class="abs" style="left:302px;top:436px" width="36" height="20" viewBox="0 0 36 20"><path d="M0 0 H36 L18 18 Z" fill="var(--banner)"/></svg>

  <div class="axis-label abs" style="top:465px">600</div>
  <div class="axis-label abs" style="top:509px">540</div>
  <div class="axis-label abs" style="top:553px">480</div>
  <div class="axis-label abs" style="top:597px">420</div>
  <div class="axis-label abs" style="top:641px">360</div>
  <div class="axis-label abs" style="top:685px">300</div>
  <div class="axis-label abs" style="top:729px">240</div>
  <div class="axis-label abs" style="top:773px">180</div>
  <div class="axis-label abs" style="top:817px">120</div>
  <div class="axis-label abs" style="top:861px">60</div>
  <div class="axis-label abs" style="top:897px">0</div>

  <svg class="abs" style="left:0;top:440px" width="640" height="470" viewBox="0 440 640 470" role="img" aria-label="Bar chart of reps per session">
    <defs>
      <linearGradient id="barGrey" x1="0" y1="0" x2="0" y2="1"><stop offset="0" stop-color="#d2d2d2"/><stop offset="1" stop-color="#bdbdbd"/></linearGradient>
      <linearGradient id="barGreen" x1="0" y1="0" x2="0" y2="1"><stop offset="0" stop-color="#a6cc2b"/><stop offset="1" stop-color="#5fbf25"/></linearGradient>
    </defs>
    <path d="M62 905 V679 a6 6 0 0 1 6 -6 H111 a6 6 0 0 1 6 6 V905Z" fill="url(#barGrey)"/>
    <path d="M147 905 V629 a6 6 0 0 1 6 -6 H196 a6 6 0 0 1 6 6 V905Z" fill="url(#barGrey)"/>
    <path d="M229 905 V656 a6 6 0 0 1 6 -6 H278 a6 6 0 0 1 6 6 V905Z" fill="url(#barGreen)"/>
    <path d="M229 660 H284 V690 Q256 700 229 690Z" fill="#7c8f1e" opacity=".55"/>
    <path d="M310 905 V719 a6 6 0 0 1 6 -6 H359 a6 6 0 0 1 6 6 V905Z" fill="url(#barGrey)"/>
    <path d="M393 905 V599 a6 6 0 0 1 6 -6 H442 a6 6 0 0 1 6 6 V905Z" fill="url(#barGrey)"/>
    <path d="M478 905 V551 a6 6 0 0 1 6 -6 H527 a6 6 0 0 1 6 6 V905Z" fill="url(#barGrey)"/>
    <path d="M562 905 V478 a6 6 0 0 1 6 -6 H611 a6 6 0 0 1 6 6 V905Z" fill="url(#barGrey)"/>
    <line x1="50" y1="905.5" x2="602" y2="905.5" stroke="#9a9a9a" stroke-width="1.5"/>
    <circle cx="256" cy="658" r="26" fill="#fff" stroke="var(--accent)" stroke-width="3"/>
    <text x="256" y="668" text-anchor="middle" font-family="Montserrat, Arial, sans-serif" font-size="27" font-weight="300" fill="var(--accent)">81</text>
  </svg>

  <div class="challenge-name abs">Example challenge</div>
  <div class="expand abs">
    <svg class="abs" style="left:30px;top:13px" width="38" height="16" viewBox="0 0 38 16"><path d="M2 2 L19 14 L36 2" fill="none" stroke="#fff" stroke-width="2.5"/></svg>
  </div>
  <div class="divider abs"></div>
  <div class="spacer abs"></div>

  <nav class="tabbar abs"></nav>
  <svg class="abs" style="left:230px;top:1008px" width="180" height="128" viewBox="0 0 180 128">
    <path d="M8 128 V90 A82 82 0 0 1 172 90 V128Z" fill="var(--header)"/>
    <path d="M12 92 A78 78 0 0 1 168 92" fill="none" stroke="#5a5f66" stroke-width="2"/>
    <path d="M73 40 L73 76 L103 58 Z" fill="var(--tab-icon)"/>
  </svg>
  <svg class="abs" style="left:32px;top:1050px" width="56" height="52" viewBox="0 0 56 52">
    <g fill="none" stroke="var(--tab-icon)" stroke-width="2.5">
      <ellipse cx="28" cy="16" rx="11" ry="14"/>
      <path d="M6 50 Q6 34 22 31 M50 50 Q50 34 34 31 M6 50 H50"/>
    </g>
  </svg>
  <svg class="abs" style="left:142px;top:1050px" width="64" height="44" viewBox="0 0 64 44">
    <path d="M4 40 L18 22 L28 30 L42 10 L50 18 L60 4" fill="none" stroke="#7ed321" stroke-width="4" stroke-linejoin="round"/>
    <path d="M4 34 L18 16 L28 24 L42 4 L50 12 L60 -2" fill="none" stroke="#7ed321" stroke-width="1.5" opacity=".6"/>
  </svg>
  <svg class="abs" style="left:444px;top:1042px" width="50" height="62" viewBox="0 0 50 62">
    <g fill="none" stroke="var(--tab-icon)" stroke-width="2.5">
      <path d="M15 34 L6 58 L14 54 L18 61 L24 40 M35 34 L44 58 L36 54 L32 61 L26 40"/>
    </g>
    <circle cx="25" cy="22" r="17" fill="var(--header)" stroke="var(--tab-icon)" stroke-width="2.5"/>
    <circle cx="25" cy="22" r="13" fill="var(--accent)"/>
    <text x="25" y="29" text-anchor="middle" font-family="Montserrat, Arial, sans-serif" font-size="19" font-weight="600" fill="#fff">2</text>
  </svg>
  <svg class="abs" style="left:552px;top:1048px" width="58" height="52" viewBox="0 0 58 52">
    <path d="M4 48 L8 24 Q12 8 24 4 L32 6 L30 14 L22 14 L18 26 Q28 18 40 22 Q54 28 52 42 Q50 50 38 50 Z" fill="none" stroke="var(--tab-icon)" stroke-width="2.5" stroke-linejoin="round"/>
  </svg>
  <div class="tab-label abs" style="left:-10px">Profile</div>
  <div class="tab-label abs active" style="left:98px">Results</div>
  <div class="tab-label abs" style="left:250px">Start</div>
  <div class="tab-label abs" style="left:398px">Challenges</div>
  <div class="tab-label abs" style="left:510px">Routines</div>

</div>
</body>
</html>
```